ROV Medisource Website design
Website design
ROV Medisource Website design -
Creative Brief
www.rovmedisource.example
Leading exporter for used medical equipments world wide
Like it to me clean and simple
left side
http://www.bluvantor.example/ http://www.torrelinkmd.example/index.html http://www.quovarent.example/en.html http://www.halbrit.example/ http://www.wellgatehub.example/ http://www.vintrosa.example/home http://www.carelodgex.example/ http://www.dorum.example/ http://www.ferntonmed.example/ http://www.zavrimedix.example/ http://www.pinehursthomes.example/ http://www.gluvatrade.example/component/page,shop.browse/category_id,8/option,com_virtuemart/Itemid,64/ (Left hand Navigation for Equipment page)

```html
<!DOCTYPE html>
<html lang="en">
<head>
<meta charset="utf-8">
<title>ROV Medisource</title>
<link rel="stylesheet" href="https://fonts.googleapis.com/css2?family=Arimo:wght@400;700&family=Tinos:wght@400;700&display=swap">
<style>
:root{
  --sky-top:#4f86c4;
  --sky-mid:#a9c9e6;
  --grass:#4f8f2c;
  --grass-light:#7fb548;
  --panel:#ffffff;
  --nav-text:#555555;
  --nav-line:#c9c9c9;
  --green-dark:#4d7d1c;
  --green:#76a834;
  --green-light:#9cc45a;
  --blue-dark:#1e5f86;
  --blue:#3a88b4;
  --blue-light:#6fb2d6;
  --orange:#f08a1c;
  --yellow:#e2c21a;
  --red:#d8352a;
  --purple:#8a3fb6;
  --logo-blue:#1a5f9c;
  --white:#ffffff;
  --footer:#f4f4f4;
}
*{margin:0;padding:0;box-sizing:border-box}
html,body{width:1200px;height:941px;overflow:hidden}
body{position:relative;font-family:"Arimo",Arial,sans-serif;color:var(--nav-text)}
.backdrop{position:absolute;inset:0;background:linear-gradient(180deg,var(--sky-top) 0%,var(--sky-mid) 45%,#b9cfe0 58%,var(--grass-light) 64%,var(--grass) 100%)}
.side-icons{position:absolute;left:247px;top:18px;width:20px}
.side-icons svg{display:block;margin-bottom:16px}
.page{position:absolute;left:280px;top:13px;width:645px;height:897px;background:var(--panel);box-shadow:0 0 8px rgba(0,0,0,.35)}
.clip{position:absolute;top:-13px;width:8px;height:30px;border-radius:4px;background:linear-gradient(90deg,#9a9a9a,#e8e8e8,#9a9a9a)}
.clip.left{left:50px}.clip.right{left:582px}

.header{position:absolute;left:5px;top:5px;width:635px;height:140px}
.logo{position:absolute;left:28px;top:30px;display:flex;align-items:center;gap:10px}
.logo-mark{width:58px;height:58px;border-radius:50%;background:var(--logo-blue)}
.logo-name{font:700 26px "Arimo",Arial,sans-serif;color:var(--logo-blue);line-height:1}
.logo-tag{position:absolute;left:96px;top:92px;font-size:8px;color:var(--green);letter-spacing:.5px}
.header-sky{position:absolute;left:315px;top:0;width:320px;height:140px;background:linear-gradient(180deg,#2f6fb6 0%,#7fb0e0 60%,#d9e9f6 100%)}

.nav{position:absolute;left:5px;top:145px;width:635px;height:118px;display:flex;border-top:1px solid var(--nav-line);border-bottom:1px solid var(--nav-line)}
.nav-item{position:relative;width:127px;height:100%;border-right:1px solid var(--nav-line);font:700 15px "Tinos",Georgia,serif;color:var(--nav-text);padding:12px 0 0 6px;letter-spacing:.5px}
.nav-item:last-child{border-right:none}
.nav-item .bar{position:absolute;left:3px;bottom:8px;width:14px;height:10px}
.nav-item.home .bar{width:120px;background:var(--green)}
.bar.blue{background:var(--blue)}.bar.yellow{background:var(--yellow)}.bar.red{background:var(--red)}.bar.purple{background:var(--purple)}
.rule{position:absolute;left:5px;top:266px;width:635px;height:4px;background:linear-gradient(90deg,var(--green),var(--green-light))}

.section-title{position:absolute;font:400 30px "Tinos",Georgia,serif;color:var(--white);display:flex;align-items:center;gap:8px}
.section-title .dot{width:22px;height:22px;border-radius:50%;border:2px solid rgba(255,255,255,.7)}

.welcome{position:absolute;left:5px;top:274px;width:635px;height:236px;background:linear-gradient(180deg,var(--green-light) 0%,var(--green) 50%,var(--green-dark) 100%)}
.welcome-photo{position:absolute;left:0;top:0;width:255px;height:236px;background:linear-gradient(180deg,#c8d6c0,#6a8b58)}
.welcome .section-title{left:260px;top:14px}
.welcome-text{position:absolute;left:270px;top:68px;width:352px;font-size:11.5px;line-height:14px;color:var(--white);text-indent:20px}
.more{position:absolute;display:inline-flex;align-items:center;gap:6px;font:700 13px "Arimo",Arial,sans-serif;color:var(--white)}
.welcome .more{left:270px;top:197px;padding:2px 10px;border:1px solid rgba(255,255,255,.6);border-radius:3px;background:rgba(0,0,0,.15)}

.offer{position:absolute;left:5px;top:516px;width:635px;height:374px;background:linear-gradient(180deg,var(--blue-light) 0%,var(--blue) 40%,var(--blue-dark) 100%)}
.offer .section-title{left:14px;top:8px;font-size:29px}
.offer-art{position:absolute;left:10px;top:50px;width:240px;height:256px;background:linear-gradient(180deg,#7dbfe0,#2f7faa)}
.offer-caption{position:absolute;left:10px;top:308px;width:240px;font-size:12px;line-height:14px;color:var(--white)}
.offer-caption::before{content:"";display:inline-block;width:8px;height:8px;background:var(--orange);margin-right:6px}
.offer-item{position:absolute;left:260px;width:370px;height:86px}
.offer-item .strip{position:absolute;left:0;top:0;width:8px;height:100%}
.offer-item .thumb{position:absolute;left:14px;top:0;width:140px;height:86px;background:linear-gradient(180deg,#f2f2f2,#cfd8de)}
.offer-item .body{position:absolute;left:160px;top:2px;width:210px;height:84px;background:rgba(255,255,255,.12)}
.offer-item h3{font:700 14px "Arimo",Arial,sans-serif;color:var(--yellow);padding:2px 4px;display:flex;align-items:center;gap:5px}
.offer-item h3::before{content:"";width:10px;height:10px;background:var(--white)}
.offer-item p{font-size:13px;line-height:15px;color:var(--white);padding:2px 8px 0}
.offer-item .more{right:8px;bottom:4px;font-size:12px}
.offer-item .more::before{content:"";width:8px;height:8px;background:var(--orange)}

.footer{position:absolute;left:0;top:914px;width:1200px;text-align:center;font:700 13px "Arimo",Arial,sans-serif;color:var(--footer)}
</style>
</head>
<body>
<div class="backdrop" role="img" aria-label="City skyline on a green lawn under a blue sky"></div>

<div class="side-icons">
  <svg width="18" height="16" viewBox="0 0 18 16"><path d="M9 1 1 8h2.5v7h4v-4h3v4h4V8H17z" fill="#fff"/></svg>
  <svg width="18" height="16" viewBox="0 0 18 16"><rect x="2" y="2" width="14" height="12" fill="none" stroke="#fff" stroke-width="2"/><path d="M6 6h6M6 10h6" stroke="#fff" stroke-width="2"/></svg>
  <svg width="18" height="14" viewBox="0 0 18 14"><rect x="1" y="1" width="16" height="12" fill="#fff"/><path d="M1 1l8 7 8-7" fill="none" stroke="#6a8fb0" stroke-width="1.5"/></svg>
</div>

<main class="page">
  <span class="clip left"></span><span class="clip right"></span>

  <header class="header">
    <div class="logo"><span class="logo-mark"></span><span class="logo-name">ROV Medisource</span></div>
    <div class="logo-tag">Partners in medical equipment</div>
    <div class="header-sky" role="img" aria-label="Blue sky with clouds"></div>
  </header>

  <nav class="nav">
    <div class="nav-item home">|HOME<span class="bar"></span></div>
    <div class="nav-item">|ABOUT<span class="bar blue"></span></div>
    <div class="nav-item">|EQUIPMENTS<span class="bar yellow"></span></div>
    <div class="nav-item">|CONSULTING<span class="bar red"></span></div>
    <div class="nav-item">|CONTACTS<span class="bar purple"></span></div>
  </nav>
  <div class="rule"></div>

  <section class="welcome">
    <div class="welcome-photo" role="img" aria-label="Two business professionals standing in front of a glass building"></div>
    <h2 class="section-title"><span class="dot"></span>Welcome ROV Medisource</h2>
    <p class="welcome-text">ROV Medisource is a Planning &amp; consulting firm that specializes in equipment planning, assessment, procurement and commissioning for health care facilities worldwide. ROV Medisource is a Planning &amp; consulting firm that specializes in equipment planning, assessment, procurement and commissioning for health care facilities worldwide.</p>
    <span class="more">more &#9662;</span>
  </section>

  <section class="offer">
    <h2 class="section-title"><span class="dot"></span>What We Offer...</h2>
    <div class="offer-art" role="img" aria-label="Surgeon in blue scrubs and cap"></div>
    <p class="offer-caption">Duis te feugifacilisi. Duis em dolor in hendrerit in vulputatelit esse molestie consequat.</p>

    <article class="offer-item" style="top:50px">
      <span class="strip" style="background:var(--orange)"></span>
      <div class="thumb" role="img" aria-label="Medical instruments"></div>
      <div class="body"><h3>UT WISI ENIM</h3><p>Ad minim veniam, quisd exerci taion.</p><span class="more">more</span></div>
    </article>
    <article class="offer-item" style="top:150px">
      <span class="strip" style="background:var(--green)"></span>
      <div class="thumb" role="img" aria-label="Pills and medicine"></div>
      <div class="body"><h3>VULPUTATE</h3><p>Sed diem nonummy nibh euismod tincidunt ut.</p><span class="more">more</span></div>
    </article>
    <article class="offer-item" style="top:250px">
      <span class="strip" style="background:var(--blue-light)"></span>
      <div class="thumb" role="img" aria-label="Gloved hands holding a syringe"></div>
      <div class="body"><h3>TEL ILLUM</h3><p>Tobortis nisl ut aliquipen commodo consequat.</p><span class="more">more</span></div>
    </article>
  </section>
</main>

<footer class="footer">ROV Medisource Inc. 2011 &copy; Copyright</footer>
</body>
</html>
```